Travel Consultant Business Card

Hello.. New travel consultant looking seeking a business card that incorporates my new logo. I specialize in cruises but also want to imply land vacation. I am very open to any design and font concepts. I'm looking for a very upbeat modern design that reflects cruise and land vacations. Bright vibrant colors

Target Market(s)

Cruise and Land Vacationers

Industry/Entity Type

Travel Agent

Contact Information for Business Card

I am very open to any design and font concepts. I'm looking for a very upbeat modern design that reflects cruise and land vacations. Bright vibrant colors

Colors

Designer to choose colors to be used in the design.

Requirements
Must have
• Company Name: PineRidge Journeys---New logo uploaded to be included in design
• My Name: Danielle Marchetti-Travel Consultant
• Phone Number: (555) 418-7093
• E-Mail Address: pineridgejourneys@mailbox-example.com
• Website: www.pineridgejourneys-example.com
Nice to have
• My tag line is …..Here to Get You There

```html
<!DOCTYPE html>
<html lang="en">
<head>
<meta charset="utf-8">
<title>PineRidge Journeys – Business Card</title>
<link href="https://fonts.googleapis.com/css2?family=Lato:wght@400;700;900&display=swap" rel="stylesheet">
<style>
  :root {
    --stage: #262626;
    --card: #1f1f1f;
    --card-edge: #2a2a2a;
    --brand-blue: #1f86d6;
    --accent-blue: #2aa4e6;
    --muted-logo: #4a4a4a;
    --text-light: #f2f2f2;
    --rule: #e8e8e8;
  }
  * { box-sizing: border-box; margin: 0; padding: 0; }
  html, body {
    width: 1200px; height: 895px; overflow: hidden;
    background: var(--stage);
    font-family: 'Lato', Arial, sans-serif;
  }
  .stage { position: relative; width: 1200px; height: 895px; }
  .card {
    position: absolute;
    width: 540px; height: 309px;
    background: linear-gradient(135deg, var(--card-edge), var(--card) 60%);
    box-shadow: 0 18px 40px rgba(0,0,0,.55);
    color: var(--text-light);
  }
  .card--front { left: 80px; top: 90px; }
  .card--back { left: 580px; top: 496px; }

  .brand-name {
    font-weight: 900;
    letter-spacing: .5px;
    white-space: nowrap;
  }
  .tagline { font-size: 15px; letter-spacing: 1px; color: var(--text-light); }

  /* front side */
  .front-mark {
    position: absolute; right: 70px; top: 56px;
    width: 78px; height: 78px; border-radius: 50%;
    background: var(--accent-blue);
  }
  .front-brand { position: absolute; left: 48px; bottom: 60px; }
  .front-brand .brand-name { font-size: 30px; color: var(--muted-logo); }
  .front-brand .tagline { margin-top: 6px; margin-left: 26px; }

  /* back side */
  .back-brand { position: absolute; left: 34px; top: 118px; width: 260px; text-align: center; }
  .back-brand .brand-name { font-size: 27px; color: var(--brand-blue); }
  .back-brand .tagline { margin-top: 8px; font-size: 14px; }

  .divider {
    position: absolute; left: 300px; top: 62px;
    width: 2px; height: 170px; background: var(--rule);
  }
  .contact { position: absolute; left: 322px; top: 70px; width: 210px; }
  .contact__name {
    font-size: 19px; font-weight: 700; color: var(--accent-blue);
    font-variant: small-caps; letter-spacing: .5px; white-space: nowrap;
  }
  .contact__role { font-size: 14px; margin-top: 2px; }
  .contact__list { list-style: none; margin-top: 22px; }
  .contact__item {
    display: flex; align-items: center; gap: 7px;
    font-size: 10.5px; line-height: 22px; white-space: nowrap;
  }
  .contact__icon { width: 11px; height: 11px; flex: none; fill: var(--accent-blue); stroke: var(--accent-blue); }
</style>
</head>
<body>
<main class="stage">

  <section class="card card--front" aria-label="Card front">
    <div class="front-mark" aria-hidden="true"></div>
    <div class="front-brand">
      <div class="brand-name">PineRidge Journeys</div>
      <div class="tagline">Here to Get You There</div>
    </div>
  </section>

  <section class="card card--back" aria-label="Card back">
    <div class="back-brand">
      <div class="brand-name">PineRidge Journeys</div>
      <div class="tagline">Here to Get You There</div>
    </div>

    <div class="divider"></div>

    <div class="contact">
      <div class="contact__name">Danielle Marchetti</div>
      <div class="contact__role">Travel Consultant</div>
      <ul class="contact__list">
        <li class="contact__item">
          <svg class="contact__icon" viewBox="0 0 12 12" aria-hidden="true"><path d="M2.5 1l2 2.5-1 1.2c.7 1.4 1.6 2.3 3 3l1.2-1 2.5 2-1.2 1.8C5 10 2 7 .8 2.2z" stroke="none"/></svg>
          (555) 418-7093
        </li>
        <li class="contact__item">
          <svg class="contact__icon" viewBox="0 0 12 12" aria-hidden="true"><rect x="0.5" y="2.5" width="11" height="7" stroke="none"/><path d="M1 3l5 3.5L11 3" fill="none" stroke="#1f1f1f" stroke-width="1"/></svg>
          pineridgejourneys@mailbox-example.com
        </li>
        <li class="contact__item">
          <svg class="contact__icon" viewBox="0 0 12 12" aria-hidden="true"><g fill="none" stroke-width="1"><circle cx="6" cy="6" r="5"/><ellipse cx="6" cy="6" rx="2.2" ry="5"/><path d="M1 6h10M2 3.5h8M2 8.5h8"/></g></svg>
          www.pineridgejourneys-example.com
        </li>
      </ul>
    </div>
  </section>

</main>
</body>
</html>
```